Community Harvest Festival Poster

Seeking a poster design to advertise our community’s annual Harvest Festival. We will utilize and display printed posters as well as distribute PDFs via our weekly e-news letters. This years "theme" is, "Brass Lantern/Pebble Lane Grove, Where Maple and Wren Unite." The vibe is a bohemian, beatnik, street scene, meets a old fashioned orchard.

Target Market(s)

NYC School Community- should appeal to an audience that ranges from kids to grandparents. Very family oriented, with wide appeal, and must be eye catching.

Font styles to use
Other font styles liked:
• One style should be more of a "Country" font, the other should have more of a clean city vibe.

Colors
acd037
ffc214
f68e4e
eaf2ce

Requirements
Must have
• The following copy:
• Brass Lantern Pebble Lane Grove
• Where Maple and Wren Unite
• Celebrate M&W With Great Food, Music, Entertainment, And Fun!
• Saturday, October 19th 2019
• 12:00-4:00pm
• Tickets will be available for sale at Drop off and Pick up
Nice to have
• I'm not limited, but a couple of ideas that could be cool:
• One incorporated the background of a street, i.e. pavement, which has leaves blowing over it, and perhaps an apple or two rolling onto the page.
• Another has a diagonal breakup of the image, with one side pavement and the other side rustic wood, also with leaves sweeping across.
• I've also attached images of previous festival posters that I have gravitated to for some idea of quality I'm looking for.
Should not have
• Anything inappropriate for children.

```html
<!DOCTYPE html>
<html lang="en">
<head>
<meta charset="utf-8">
<title>Brass Lantern Pebble Lane Grove – Harvest Festival</title>
<link rel="stylesheet" href="https://fonts.googleapis.com/css2?family=Sancreek&family=Montserrat:wght@600;700&display=swap">
<style>
  :root {
    --pavement-light: #3a4850;
    --pavement-dark: #1c262b;
    --leaf-red: #b8322a;
    --leaf-orange: #d9702a;
    --leaf-gold: #d9a232;
    --apple-red: #c23a30;
    --ink-white: #f4f4f1;
    --ribbon-gold: #f7a823;
    --ribbon-fold: #d9262c;
    --ribbon-text: #24303a;
    --accent-orange: #f7a51d;
  }
  * { margin: 0; padding: 0; box-sizing: border-box; }
  html, body {
    width: 848px;
    height: 1200px;
    overflow: hidden;
    background: var(--pavement-dark);
  }
  .poster {
    position: relative;
    width: 848px;
    height: 1200px;
    overflow: hidden;
    font-family: "Montserrat", Arial, sans-serif;
    color: var(--ink-white);
  }
  .backdrop-pavement {
    position: absolute;
    inset: 0;
    background:
      radial-gradient(ellipse at 40% 35%, var(--pavement-light) 0%, rgba(58,72,80,0) 65%),
      linear-gradient(160deg, #2f3d44 0%, #26333a 55%, var(--pavement-dark) 100%);
  }
  .harvest-scatter {
    position: absolute;
    inset: 0;
    background:
      radial-gradient(circle at 190px 632px, rgba(194,58,48,0.85) 0, rgba(194,58,48,0.55) 70px, rgba(194,58,48,0) 100px),
      radial-gradient(ellipse 120px 110px at 535px 595px, rgba(217,162,50,0.7) 0, rgba(217,112,42,0.35) 60%, rgba(217,112,42,0) 100%),
      radial-gradient(ellipse 90px 40px at 345px 510px, rgba(217,162,50,0.55) 0, rgba(217,162,50,0) 100%),
      radial-gradient(ellipse 120px 90px at 165px 380px, rgba(217,112,42,0.55) 0, rgba(217,112,42,0) 100%),
      radial-gradient(ellipse 120px 90px at 760px 400px, rgba(184,50,42,0.6) 0, rgba(184,50,42,0) 100%),
      radial-gradient(ellipse 60px 120px at 30px 600px, rgba(184,50,42,0.55) 0, rgba(184,50,42,0) 100%),
      radial-gradient(ellipse 80px 110px at 760px 90px, rgba(217,112,42,0.45) 0, rgba(217,112,42,0) 100%),
      radial-gradient(ellipse 60px 40px at 725px 585px, rgba(217,112,42,0.45) 0, rgba(217,112,42,0) 100%),
      radial-gradient(ellipse 40px 40px at 260px 850px, rgba(184,90,50,0.45) 0, rgba(184,90,50,0) 100%),
      radial-gradient(ellipse 40px 28px at 478px 948px, rgba(184,70,42,0.5) 0, rgba(184,70,42,0) 100%),
      radial-gradient(ellipse 50px 50px at 240px 1080px, rgba(120,40,30,0.55) 0, rgba(120,40,30,0) 100%),
      radial-gradient(circle at 675px 1068px, rgba(194,58,48,0.85) 0, rgba(194,58,48,0.55) 60px, rgba(194,58,48,0) 90px),
      radial-gradient(ellipse 50px 60px at 815px 1100px, rgba(140,60,40,0.5) 0, rgba(140,60,40,0) 100%);
  }
  .vine-ornament {
    position: absolute;
    left: 636px;
    top: 705px;
    width: 212px;
    height: 305px;
    background: radial-gradient(ellipse at 70% 50%, rgba(247,165,29,0.55) 0%, rgba(247,165,29,0) 70%);
  }
  .title {
    position: absolute;
    left: 0;
    top: 78px;
    width: 848px;
    text-align: center;
    font-family: "Sancreek", Georgia, serif;
    font-weight: 400;
    color: var(--ink-white);
    white-space: nowrap;
    line-height: 1;
  }
  .title-line { display: block; }
  .title-small { font-size: 66px; }
  .title-mid { font-size: 94px; margin-top: 20px; }
  .title-large { font-size: 130px; margin-top: 14px; }
  .ribbon {
    position: absolute;
    left: 172px;
    top: 438px;
    width: 512px;
    height: 66px;
  }
  .ribbon svg { position: absolute; inset: 0; }
  .ribbon-text {
    position: absolute;
    left: 0;
    top: 8px;
    width: 512px;
    text-align: center;
    font-weight: 700;
    font-size: 22px;
    color: var(--ribbon-text);
    text-transform: uppercase;
    white-space: nowrap;
  }
  .tagline {
    position: absolute;
    left: 0;
    top: 734px;
    width: 848px;
    text-align: center;
    font-weight: 700;
    font-size: 32px;
    line-height: 36px;
  }
  .info-icon { position: absolute; }
  .icon-clock { left: 78px; top: 928px; }
  .icon-ticket { left: 315px; top: 936px; }
  .info-text {
    position: absolute;
    top: 1013px;
    font-weight: 700;
    font-size: 21.5px;
    line-height: 35px;
    white-space: nowrap;
  }
  .info-date { left: 53px; }
  .info-tickets { left: 320px; }
</style>
</head>
<body>
<main class="poster">
  <div class="backdrop-pavement"></div>
  <div class="harvest-scatter" role="img" aria-label="Photograph of dark weathered pavement with scattered red, orange and yellow autumn leaves, a red apple at left centre and another at lower right"></div>
  <div class="vine-ornament" role="img" aria-label="Orange leafy vine ornament curling in from the right edge"></div>

  <h1 class="title">
    <span class="title-line title-small">Brass Lantern</span>
    <span class="title-line title-mid">Pebble Lane</span>
    <span class="title-line title-large">Grove</span>
  </h1>

  <div class="ribbon">
    <svg width="512" height="66" viewBox="0 0 512 66" aria-hidden="true">
      <polygon points="0,38 26,38 26,62 8,62" fill="var(--ribbon-fold)"/>
      <polygon points="512,38 486,38 486,62 504,62" fill="var(--ribbon-fold)"/>
      <rect x="8" y="0" width="496" height="46" fill="var(--ribbon-gold)"/>
    </svg>
    <p class="ribbon-text">Where Maple and Wren Unite</p>
  </div>

  <p class="tagline">Celebrate M&amp;W With Great<br>Food, Music, Entertainment,<br>And Fun!</p>

  <svg class="info-icon icon-clock" width="66" height="66" viewBox="0 0 66 66" aria-hidden="true">
    <circle cx="33" cy="33" r="28" fill="none" stroke="var(--accent-orange)" stroke-width="6"/>
    <polyline points="30,17 30,37 44,37" fill="none" stroke="var(--accent-orange)" stroke-width="5"/>
  </svg>
  <svg class="info-icon icon-ticket" width="92" height="48" viewBox="0 0 92 48" aria-hidden="true">
    <path d="M10 3 H82 L89 10 V38 L82 45 H10 L3 38 V10 Z" fill="none" stroke="var(--accent-orange)" stroke-width="5"/>
  </svg>

  <p class="info-text info-date">Saturday,<br>October 19th 2019<br>12:00-4:00pm</p>
  <p class="info-text info-tickets">Tickets will be available<br>for sale at Drop off<br>and Pick up</p>
</main>
</body>
</html>
```